Talon Microchips PowerPoint Master Slide Deck Design

This is a 2-phase project to design a slide deck for a semiconductor company in the Silicon Valley. The design budget will be increased with each phase.
The slide deck will need to have one version with a dark background for presentations and a second version with a white background. Otherwise, the slides will be the same. I anticipate we will need a total of 10 slides, but that number may change.
The first phase will be to design a Title and a Title and Content slide.
- The Title Slide is the first slide of the deck. It should include the presentation title, the presenter's name and date of presentation
- The Title and Content slide should include a title and content with bullet points and up to 2 additional sub-bullets
- The Title and Content slide should have a footer that includes the slide #, Talon Microchips Confidential, and the logo. This footer will be on every slide except the Title Slide
The first two slides will serve as the format for the remaining ~8 slides:
-Header and Content Text (1, 2, 4 column)
-Header and Content Image (bar chart, pie chart, tables)
-Break
-Title only
-Closing (Talon logo only)
Our slides contain a lot of content so a clean and simple design is best.
Both phases will need to include pre-set color options for
-Text and Lines
-Shadows
-Bullets and sub-bullets (including shapes, ex. circle, slash, square, etc.)
-Bar charts, pie charts, tables
Samples of our collateral are attached. Logo files are also attached

```html
<!DOCTYPE html>
<html lang="en">
<head>
<meta charset="utf-8">
<title>Talon Microchips – Master Slide Deck</title>
<link href="https://fonts.googleapis.com/css2?family=Montserrat:ital,wght@0,400;0,500;0,600;0,700;0,800;1,700;1,800&display=swap" rel="stylesheet">
<style>
:root{
  --board:#1b1b1b;
  --blue-1:#0a22ff;
  --blue-2:#1c5cf4;
  --blue-deep:#0547c4;
  --accent:#5ec8f0;
  --white:#ffffff;
  --line-soft:rgba(255,255,255,.55);
  --line-faint:rgba(255,255,255,.28);
}
*{box-sizing:border-box;margin:0;padding:0}
html,body{width:804px;height:1200px;overflow:hidden;background:var(--board)}
body{position:relative;font-family:'Montserrat',sans-serif;color:var(--white)}

.slide{position:absolute;width:697px;height:392px;transform:scale(.5136);transform-origin:0 0;overflow:hidden;
  background:linear-gradient(125deg,var(--blue-1) 0%,#0e35fb 55%,var(--blue-2) 100%)}
.col-l{left:30px}.col-r{left:416px}
.row-1{top:35px}.row-2{top:267px}.row-3{top:499px}.row-4{top:732px}.row-5{top:964px}

.abs{position:absolute}
.rule{position:absolute;height:2px;width:67px;background:var(--white)}
.slide-title{position:absolute;font-weight:700;font-size:35px;letter-spacing:3px;white-space:nowrap;line-height:1}
.hl{color:var(--accent)}

/* footer */
.footer{position:absolute;left:0;right:0;bottom:0;height:44px}
.footer-line{position:absolute;left:12px;right:12px;top:0;height:1px;background:var(--line-faint)}
.footer-tick{position:absolute;left:347px;top:-2px;width:3px;height:5px;background:var(--line-soft)}
.footer-brand{position:absolute;left:96px;top:14px;font-weight:700;font-size:11px}
.footer-copy{position:absolute;left:230px;top:16px;font-size:9px;letter-spacing:1.6px}
.footer-num{position:absolute;left:570px;top:16px;font-size:9px;font-weight:700;letter-spacing:1.2px}

/* boxes */
.box{position:absolute;border:1px solid var(--line-soft)}
.num{position:absolute;font-weight:700;line-height:1}
.bul{position:absolute;display:flex;align-items:flex-start;gap:8px}
.bul svg{flex:none;margin-top:2px}

/* title slide */
.title-bar{position:absolute;left:124px;top:82px;width:3px;height:228px;background:var(--white)}
.brand-name{position:absolute;left:153px;top:98px;font-weight:600;font-size:26px}
.deck-title{position:absolute;left:153px;top:168px;font-weight:800;font-size:42px;line-height:52px;letter-spacing:1px}
.meta{position:absolute;top:292px;font-weight:600;font-size:12.5px;letter-spacing:3px}
.meta-divider{position:absolute;left:368px;top:286px;width:2px;height:26px;background:var(--white)}

.ring{position:absolute;border-radius:50%}
.chart-card{position:absolute;left:47px;top:145px;width:296px;height:173px;background:#fff;box-shadow:0 4px 12px rgba(0,0,0,.25)}
.bar{position:absolute;top:149px;width:27px;height:158px;background:#fff}
.bar-fill{position:absolute;left:0;right:0;bottom:0;background:var(--accent);font-size:8px;font-weight:700;text-align:center;padding-top:6px}
.year{position:absolute;top:314px;width:40px;text-align:center;font-size:9px;font-weight:700}
</style>
</head>
<body>

<!-- 1 Title -->
<section class="slide col-l row-1">
  <div class="title-bar"></div>
  <div class="brand-name">Talon Microchips</div>
  <h1 class="deck-title">BUSINESS<br>PRESENTATION</h1>
  <div class="meta" style="left:153px">PRESENTER’S NAME</div>
  <div class="meta-divider"></div>
  <div class="meta" style="left:398px;letter-spacing:1.5px">DATE: 12-20-2024</div>
</section>

<!-- 2 Four boxes -->
<section class="slide col-r row-1">
  <div class="rule" style="left:118px;top:43px"></div>
  <h2 class="slide-title" style="left:118px;top:58px">YOUR <span class="hl">CONTENT</span> SLIDE</h2>
  <div class="box" style="left:42px;top:122px;width:301px;height:87px"></div>
  <div class="box" style="left:354px;top:122px;width:302px;height:87px"></div>
  <div class="box" style="left:42px;top:221px;width:301px;height:87px"></div>
  <div class="box" style="left:354px;top:221px;width:302px;height:87px"></div>
  <div class="num" style="left:56px;top:153px;font-size:40px">01</div>
  <div class="num" style="left:368px;top:153px;font-size:40px">02</div>
  <div class="num" style="left:56px;top:252px;font-size:40px">03</div>
  <div class="num" style="left:368px;top:252px;font-size:40px">04</div>
  <div class="abs" style="left:130px;top:136px;width:200px">
    <div style="font-weight:700;font-size:12.5px">CONTENT HEADER</div>
    <div style="font-size:5.5px;margin-top:4px">Lorem ipsum dolor sit amet, consectetuer adipiscing elit. Aenean commodo ligula eget dolor. Aenean massa.</div>
    <div style="font-size:5.5px;margin:4px 0 0 14px">⊸ Lorem ipsum dolor sit amet, consectetuer adipiscing elit.</div>
    <div style="font-size:5.5px;margin:4px 0 0 14px">⊸ Lorem ipsum dolor sit amet, consectetuer adipiscing elit.</div>
  </div>
  <div class="abs" style="left:443px;top:136px;width:200px">
    <div style="font-weight:700;font-size:12.5px">CONTENT HEADER</div>
    <div style="font-size:5.5px;margin-top:4px">Lorem ipsum dolor sit amet, consectetuer adipiscing elit. Aenean commodo ligula eget dolor. Aenean massa.</div>
    <div style="font-size:5.5px;margin:4px 0 0 14px">⊸ Lorem ipsum dolor sit amet, consectetuer adipiscing elit.</div>
    <div style="font-size:5.5px;margin:4px 0 0 14px">⊸ Lorem ipsum dolor sit amet, consectetuer adipiscing elit.</div>
  </div>
  <div class="abs" style="left:130px;top:235px;width:200px">
    <div style="font-weight:700;font-size:12.5px">CONTENT HEADER</div>
    <div style="font-size:5.5px;margin-top:4px">Lorem ipsum dolor sit amet, consectetuer adipiscing elit. Aenean commodo ligula eget dolor. Aenean massa.</div>
    <div style="font-size:5.5px;margin:4px 0 0 14px">⊸ Lorem ipsum dolor sit amet, consectetuer adipiscing elit.</div>
    <div style="font-size:5.5px;margin:4px 0 0 14px">⊸ Lorem ipsum dolor sit amet, consectetuer adipiscing elit.</div>
  </div>
  <div class="abs" style="left:443px;top:235px;width:200px">
    <div style="font-weight:700;font-size:12.5px">CONTENT HEADER</div>
    <div style="font-size:5.5px;margin-top:4px">Lorem ipsum dolor sit amet, consectetuer adipiscing elit. Aenean commodo ligula eget dolor. Aenean massa.</div>
    <div style="font-size:5.5px;margin:4px 0 0 14px">⊸ Lorem ipsum dolor sit amet, consectetuer adipiscing elit.</div>
    <div style="font-size:5.5px;margin:4px 0 0 14px">⊸ Lorem ipsum dolor sit amet, consectetuer adipiscing elit.</div>
  </div>
  <footer class="footer"><div class="footer-line"></div><div class="footer-tick"></div><div class="footer-brand">Talon</div><div class="footer-copy">©Copyright 2023 Talon Microchips.</div><div class="footer-num">SLIDE #</div></footer>
</section>

<!-- 3 Two rows -->
<section class="slide col-l row-2">
  <div class="rule" style="left:90px;top:43px"></div>
  <h2 class="slide-title" style="left:90px;top:58px">CONTENT <span class="hl">HEADER</span> SLIDE</h2>
  <div class="box" style="left:47px;top:108px;width:603px;height:110px"></div>
  <div class="box" style="left:47px;top:223px;width:603px;height:111px"></div>
  <div class="num" style="left:70px;top:146px;font-size:38px">01</div>
  <div class="num" style="left:70px;top:262px;font-size:38px">02</div>
  <div class="abs" style="left:158px;top:120px;width:470px;font-size:12.5px;line-height:15px">Lorem ipsum dolor sit amet, consectetuer adipiscing elit. Aenean commodo ligula eget dolor. Aenean massa.</div>
  <div class="bul" style="left:203px;top:172px;font-size:12px"><svg width="16" height="8"><path d="M0 4H10" stroke="#fff" stroke-width="1.5"/><circle cx="12.5" cy="4" r="2.5" fill="none" stroke="#fff" stroke-width="1.5"/></svg>Lorem ipsum dolor sit amet, consectetuer adipiscing elit.</div>
  <div class="bul" style="left:203px;top:195px;font-size:12px"><svg width="16" height="8"><path d="M0 4H10" stroke="#fff" stroke-width="1.5"/><circle cx="12.5" cy="4" r="2.5" fill="none" stroke="#fff" stroke-width="1.5"/></svg>Lorem ipsum dolor sit amet, consectetuer adipiscing elit.</div>
  <div class="abs" style="left:158px;top:234px;width:470px;font-size:12.5px;line-height:15px">Lorem ipsum dolor sit amet, consectetuer adipiscing elit. Aenean commodo ligula eget dolor. Aenean massa.</div>
  <div class="bul" style="left:203px;top:282px;font-size:12px"><svg width="16" height="8"><path d="M0 4H10" stroke="#fff" stroke-width="1.5"/><circle cx="12.5" cy="4" r="2.5" fill="none" stroke="#fff" stroke-width="1.5"/></svg>Lorem ipsum dolor sit amet, consectetuer adipiscing elit.</div>
  <div class="bul" style="left:203px;top:305px;font-size:12px"><svg width="16" height="8"><path d="M0 4H10" stroke="#fff" stroke-width="1.5"/><circle cx="12.5" cy="4" r="2.5" fill="none" stroke="#fff" stroke-width="1.5"/></svg>Lorem ipsum dolor sit amet, consectetuer adipiscing elit.</div>
  <footer class="footer"><div class="footer-line"></div><div class="footer-tick"></div><div class="footer-brand">Talon</div><div class="footer-copy">©Copyright 2023 Talon Microchips.</div><div class="footer-num">SLIDE #</div></footer>
</section>

<!-- 4 Two columns -->
<section class="slide col-r row-2">
  <div class="rule" style="left:91px;top:43px"></div>
  <h2 class="slide-title" style="left:91px;top:58px">CONTENT <span class="hl">HEADER</span> SLIDE</h2>
  <div class="box" style="left:42px;top:110px;width:302px;height:219px"></div>
  <div class="box" style="left:360px;top:110px;width:302px;height:219px"></div>
  <div class="num" style="left:57px;top:142px;font-size:36px">01</div>
  <div class="num" style="left:375px;top:142px;font-size:36px">02</div>
  <div class="abs" style="left:120px;top:138px;width:210px;font-size:12.5px;line-height:15.5px">Lorem ipsum dolor sit amet, consectetuer adipiscing elit. Aenean commodo ligula eget dolor. Aenean massa.</div>
  <div class="abs" style="left:438px;top:138px;width:210px;font-size:12.5px;line-height:15.5px">Lorem ipsum dolor sit amet, consectetuer adipiscing elit. Aenean commodo ligula eget dolor. Aenean massa.</div>
  <div class="bul" style="left:120px;top:223px;width:200px;font-size:11.5px;line-height:14px"><svg width="22" height="10"><path d="M0 5H14" stroke="#fff" stroke-width="1.5"/><circle cx="17" cy="5" r="3" fill="none" stroke="#fff" stroke-width="1.5"/></svg>Lorem ipsum dolor sit amet, consectetuer adipiscing elit.</div>
  <div class="bul" style="left:120px;top:268px;width:200px;font-size:11.5px;line-height:14px"><svg width="22" height="10"><path d="M0 5H14" stroke="#fff" stroke-width="1.5"/><circle cx="17" cy="5" r="3" fill="none" stroke="#fff" stroke-width="1.5"/></svg>Lorem ipsum dolor sit amet, consectetuer adipiscing elit.</div>
  <div class="bul" style="left:438px;top:223px;width:200px;font-size:11.5px;line-height:14px"><svg width="22" height="10"><path d="M0 5H14" stroke="#fff" stroke-width="1.5"/><circle cx="17" cy="5" r="3" fill="none" stroke="#fff" stroke-width="1.5"/></svg>Lorem ipsum dolor sit amet, consectetuer adipiscing elit.</div>
  <div class="bul" style="left:438px;top:268px;width:200px;font-size:11.5px;line-height:14px"><svg width="22" height="10"><path d="M0 5H14" stroke="#fff" stroke-width="1.5"/><circle cx="17" cy="5" r="3" fill="none" stroke="#fff" stroke-width="1.5"/></svg>Lorem ipsum dolor sit amet, consectetuer adipiscing elit.</div>
  <footer class="footer"><div class="footer-line"></div><div class="footer-tick"></div><div class="footer-brand">Talon</div><div class="footer-copy">©Copyright 2023 Talon Microchips.</div><div class="footer-num">SLIDE #</div></footer>
</section>

<!-- 5 Four columns -->
<section class="slide col-l row-3">
  <div class="rule" style="left:90px;top:43px"></div>
  <h2 class="slide-title" style="left:90px;top:58px">CONTENT <span class="hl">HEADER</span> SLIDE</h2>
  <div class="abs" style="left:353px;top:125px;width:1px;height:140px;background:var(--line-faint)"></div>
  <div class="abs" style="left:195px;top:125px;width:1px;height:140px;background:var(--line-faint)"></div>
  <div class="abs" style="left:512px;top:125px;width:1px;height:140px;background:var(--line-faint)"></div>

  <div class="num" style="left:53px;top:124px;font-size:36px">01</div>
  <svg class="abs" style="left:113px;top:128px" width="52" height="24" fill="none" stroke="#fff" stroke-width="1.5"><circle cx="10" cy="7" r="5"/><circle cx="26" cy="7" r="5"/><circle cx="42" cy="7" r="5"/><path d="M2 22a8 8 0 0 1 16 0M18 22a8 8 0 0 1 16 0M34 22a8 8 0 0 1 16 0"/></svg>
  <div class="num" style="left:224px;top:124px;font-size:36px">02</div>
  <svg class="abs" style="left:284px;top:128px" width="26" height="26" fill="none" stroke="#fff" stroke-width="1.5"><circle cx="13" cy="13" r="11"/><path d="M13 7v6l4 3"/></svg>
  <div class="num" style="left:374px;top:124px;font-size:36px">03</div>
  <svg class="abs" style="left:436px;top:126px" width="26" height="28" fill="none" stroke="#fff" stroke-width="1.5"><path d="M13 2c6 4 7 12 3 18h-6C6 14 7 6 13 2z"/><circle cx="13" cy="11" r="2.5"/><path d="M10 20l-4 5M16 20l4 5"/></svg>
  <div class="num" style="left:518px;top:124px;font-size:36px">04</div>
  <svg class="abs" style="left:580px;top:128px" width="32" height="26" fill="none" stroke="#fff" stroke-width="1.5"><path d="M16 2c8 0 14 4 14 10s-6 10-14 10c-2 0-4 0-6-1l-6 3 2-5C3 17 2 14 2 12 2 6 8 2 16 2z"/><path d="M10 10h12M10 14h8"/></svg>

  <div class="abs" style="left:48px;top:165px;width:135px;font-size:10.5px">
    <div style="font-weight:700;font-size:11.5px;letter-spacing:.5px">Subsection Title</div>
    <div style="margin-top:22px;line-height:10.5px">Lorem ipsum dolor sit amet, consectetuer adipiscing elit. Aenean commodo ligula eget dolor. Aenean massa.</div>
    <div style="font-size:6.5px;margin:10px 0 0 24px">Lorem ipsum dolor sit amet, consectetuer adipiscing elit.</div>
    <div style="font-size:6.5px;margin:12px 0 0 24px">Lorem ipsum dolor sit amet, consectetuer adipiscing elit.</div>
  </div>
  <div class="abs" style="left:207px;top:165px;width:135px;font-size:10.5px">
    <div style="font-weight:700;font-size:11.5px;letter-spacing:.5px">Subsection Title</div>
    <div style="margin-top:22px;line-height:10.5px">Lorem ipsum dolor sit amet, consectetuer adipiscing elit. Aenean commodo ligula eget dolor. Aenean massa.</div>
    <div style="font-size:6.5px;margin:10px 0 0 24px">Lorem ipsum dolor sit amet, consectetuer adipiscing elit.</div>
    <div style="font-size:6.5px;margin:12px 0 0 24px">Lorem ipsum dolor sit amet, consectetuer adipiscing elit.</div>
  </div>
  <div class="abs" style="left:366px;top:165px;width:135px;font-size:10.5px">
    <div style="font-weight:700;font-size:11.5px;letter-spacing:.5px">Subsection Title</div>
    <div style="margin-top:22px;line-height:10.5px">Lorem ipsum dolor sit amet, consectetuer adipiscing elit. Aenean commodo ligula eget dolor. Aenean massa.</div>
    <div style="font-size:6.5px;margin:10px 0 0 24px">Lorem ipsum dolor sit amet, consectetuer adipiscing elit.</div>
    <div style="font-size:6.5px;margin:12px 0 0 24px">Lorem ipsum dolor sit amet, consectetuer adipiscing elit.</div>
  </div>
  <div class="abs" style="left:525px;top:165px;width:135px;font-size:10.5px">
    <div style="font-weight:700;font-size:11.5px;letter-spacing:.5px">Subsection Title</div>
    <div style="margin-top:22px;line-height:10.5px">Lorem ipsum dolor sit amet, consectetuer adipiscing elit. Aenean commodo ligula eget dolor. Aenean massa.</div>
    <div style="font-size:6.5px;margin:10px 0 0 24px">Lorem ipsum dolor sit amet, consectetuer adipiscing elit.</div>
    <div style="font-size:6.5px;margin:12px 0 0 24px">Lorem ipsum dolor sit amet, consectetuer adipiscing elit.</div>
  </div>
  <footer class="footer"><div class="footer-line"></div><div class="footer-tick"></div><div class="footer-brand">Talon</div><div class="footer-copy">©Copyright 2023 Talon Microchips.</div><div class="footer-num">SLIDE #</div></footer>
</section>

<!-- 6 Content with image -->
<section class="slide col-r row-3">
  <div class="ring" style="left:298px;top:-191px;width:514px;height:514px;background:var(--white)"></div>
  <div class="ring" role="img" aria-label="Image placeholder" style="left:363px;top:-126px;width:384px;height:384px;background:linear-gradient(120deg,#0a22ff 0%,var(--blue-deep) 100%)"></div>
  <div class="abs" style="left:450px;top:92px;font-weight:700;font-size:20px;line-height:24px;letter-spacing:1px">PLACE YOUR<br>IMAGE HERE</div>
  <div class="rule" style="left:77px;top:112px;width:66px"></div>
  <h2 class="abs" style="left:73px;top:126px;font-weight:700;font-size:35px;line-height:43px;letter-spacing:2px">CONTENT<br><span class="hl">HEADER</span><br>SLIDE</h2>
  <footer class="footer"><div class="footer-line"></div><div class="footer-tick"></div><div class="footer-brand">Talon</div><div class="footer-copy">©Copyright 2023 Talon Microchips.</div><div class="footer-num">SLIDE #</div></footer>
</section>

<!-- 7 Charts -->
<section class="slide col-l row-4">
  <div class="rule" style="left:90px;top:43px"></div>
  <h2 class="slide-title" style="left:90px;top:58px">CONTENT <span class="hl">HEADER</span> SLIDE</h2>
  <div class="abs" style="left:0;right:0;top:112px;text-align:center;font-size:12px">YOUR CONTENT GRAPHS STYLE</div>
  <div class="chart-card">
    <svg class="abs" style="left:14px;top:14px" width="110" height="60">
      <g stroke="#e3e8f0" stroke-width=".5"><path d="M8 8H108M8 20H108M8 32H108M8 44H108"/></g>
      <rect x="20" y="18" width="3" height="36" fill="#0b2a8a"/><rect x="25" y="26" width="3" height="28" fill="#5ec8f0"/>
      <rect x="44" y="46" width="3" height="8" fill="#0b2a8a"/><rect x="49" y="34" width="3" height="20" fill="#5ec8f0"/>
      <rect x="68" y="12" width="3" height="42" fill="#0b2a8a"/><rect x="73" y="44" width="3" height="10" fill="#5ec8f0"/>
      <rect x="92" y="20" width="3" height="34" fill="#0b2a8a"/><rect x="97" y="48" width="3" height="6" fill="#5ec8f0"/>
    </svg>
    <div class="abs" style="left:152px;top:18px;width:130px;color:#1b4fe0">
      <div style="font-size:8px">Lorem ipsum</div>
      <div style="font-size:4px;color:#5a6275;margin-top:3px">Lorem ipsum dolor sit amet, consectetuer adipiscing elit, sed diam nonummy nibh euismod tincidunt ut laoreet dolore magna aliquam erat volutpat. Ut wisi enim ad minim veniam, quis nostrud.</div>
    </div>
    <div class="abs" style="left:18px;top:108px;width:112px;text-align:center;color:#1b4fe0">
      <div style="font-size:8px">Lorem ipsum</div>
      <div style="font-size:4px;color:#5a6275;margin-top:3px">Lorem ipsum dolor sit amet, consectetuer adipiscing elit, sed diam nonummy nibh euismod tincidunt ut laoreet dolore magna aliquam erat volutpat. Ut wisi enim ad minim veniam.</div>
    </div>
    <svg class="abs" style="left:146px;top:100px" width="140" height="60">
      <g stroke="#e3e8f0" stroke-width=".5"><path d="M6 8H136M6 20H136M6 32H136M6 44H136"/></g>
      <polyline points="10,50 26,38 42,30 58,14 74,32 90,24 106,36 122,22" fill="none" stroke="#0b2a8a" stroke-width="1"/>
      <polyline points="10,44 26,46 42,28 58,34 74,20 90,38 106,28 122,40" fill="none" stroke="#5ec8f0" stroke-width="1"/>
    </svg>
  </div>
  <div class="bar" style="left:385px"><div class="bar-fill" style="height:15%">15%</div></div>
  <div class="bar" style="left:428px"><div class="bar-fill" style="height:25%">25%</div></div>
  <div class="bar" style="left:470px"><div class="bar-fill" style="height:35%">35%</div></div>
  <div class="bar" style="left:512px"><div class="bar-fill" style="height:55%">55%</div></div>
  <div class="bar" style="left:555px"><div class="bar-fill" style="height:65%">65%</div></div>
  <div class="bar" style="left:598px"><div class="bar-fill" style="height:75%">75%</div></div>
  <div class="year" style="left:378px">2019</div><div class="year" style="left:421px">2020</div><div class="year" style="left:463px">2021</div>
  <div class="year" style="left:505px">2022</div><div class="year" style="left:548px">2023</div><div class="year" style="left:591px">2024</div>
  <footer class="footer"><div class="footer-line"></div><div class="footer-tick"></div><div class="footer-brand">Talon</div><div class="footer-copy">©Copyright 2023 Talon Microchips.</div><div class="footer-num">SLIDE #</div></footer>
</section>

<!-- 8 Break -->
<section class="slide col-r row-4">
  <svg class="abs" style="left:298px;top:82px" width="100" height="100" fill="none" stroke="#fff" stroke-width="2.2" stroke-linecap="round">
    <path d="M24 8c-4 4 4 8 0 12s4 8 0 12M40 8c-4 4 4 8 0 12s4 8 0 12M56 8c-4 4 4 8 0 12s4 8 0 12"/>
    <path d="M14 46h52v20c0 12-8 20-20 20h-12c-12 0-20-8-20-20z"/>
    <path d="M66 52h6a8 8 0 0 1 0 16h-7"/>
    <path d="M5 96h68"/>
    <rect x="33" y="58" width="12" height="16"/>
  </svg>
  <h2 class="abs" style="left:0;right:0;top:196px;text-align:center;font-weight:800;font-size:35px;letter-spacing:2px">BREAK <span class="hl" style="font-style:italic">SLIDE</span></h2>
  <footer class="footer"><div class="footer-line"></div><div class="footer-tick"></div><div class="footer-brand">Talon</div><div class="footer-copy">©Copyright 2023 Talon Microchips.</div><div class="footer-num">SLIDE #</div></footer>
</section>

<!-- 9 Title only -->
<section class="slide col-l row-5">
  <div class="ring" style="left:362px;top:-490px;width:660px;height:660px;background:var(--white)"></div>
  <div class="ring" style="left:442px;top:-410px;width:500px;height:500px;background:linear-gradient(120deg,#0d30ff,var(--blue-deep))"></div>
  <div class="ring" style="left:-265px;top:145px;width:450px;height:450px;background:var(--white)"></div>
  <div class="ring" style="left:-200px;top:210px;width:320px;height:320px;background:linear-gradient(120deg,#0a28f8,var(--blue-deep))"></div>
  <h1 class="abs" style="left:200px;top:142px;font-weight:800;font-size:40px;line-height:52px;letter-spacing:1px">YOUR TITLE<br>SLIDE</h1>
  <footer class="footer" style="background:linear-gradient(90deg,#0f3cff,#1c5cf4)"><div class="footer-line"></div><div class="footer-tick"></div><div class="footer-brand">Talon</div><div class="footer-copy">©Copyright 2023 Talon Microchips.</div><div class="footer-num">SLIDE #</div></footer>
</section>

<!-- 10 Closing -->
<section class="slide col-r row-5">
  <div class="ring" style="left:398px;top:-540px;width:660px;height:660px;background:var(--white)"></div>
  <div class="ring" style="left:478px;top:-460px;width:500px;height:500px;background:linear-gradient(120deg,#0d30ff,var(--blue-deep))"></div>
  <div class="abs" style="left:0;right:0;top:158px;text-align:center;font-weight:700;font-size:56px;letter-spacing:1px">Talon Microchips</div>
  <footer class="footer"><div class="footer-line"></div><div class="footer-tick"></div><div class="footer-brand">Talon</div><div class="footer-copy">©Copyright 2023 Talon Microchips.</div><div class="footer-num">SLIDE #</div></footer>
</section>

</body>
</html>
```